TotHaven Community Landing Page

TotHaven is a virtual world built with childrens' needs in mind. It is an online portal where parents will find all kids' related stuffs and a community connect point for parents to interact and share their experiences.

We need the designs for 2 pages within TotHaven:
- Landing Page for the Community Area
- Registration page for membership

1) The Landing Page need to have the following:

Logo & Main Background :- use the images attached

Page Title & Navigation Menu :-
The page title is "Community Connect"; navigation menu should be able to hold at least 6 tabs

Login Widget* :-
We want to put emphasis on the design of this.
For visitors, this is a normal login widget with username/password input fields, register button and 'login with chatterbook' button.
For logged-in users, this becomes a simple dashboard widget with Avatar, shortlinks and some useful navigation buttons.

"Groups" Section :-
This area holds an image, a short paragraph introducing "Groups", a widget showing 5-10 latest/popular groups and a 'Go to Groups' button at the bottom.

"Forum" Section :-
This area holds an image, a short paragraph introducing "Forum", a widget showing 5-10 latest/popular discussion topics and a 'Go to Forum' button at the bottom.

"Activities" Section -
This area holds an image, a short paragraph introducing "Forum", a widget showing 5-10 latest/popular events & activities and a 'Go to Activities' button at the bottom.

"Marketplace" Section :-
This area holds an image, a short paragraph introducing "Marketplace", a widget showing 5-10 latest/popular products and a 'Go to Marketplace' button at the bottom.

Social Media elements :-
The usual social media icons and chatterbook like box.

2) The Registration Page will need to contain the registration form as per the image attached.

Target Market(s)

Parents with kids ranging from 2 - 12 years old

Industry/Entity Type

Events

Requirements
Nice to have
• - colorful illustrations of kids or kids related images all around

```html
<!DOCTYPE html>
<html lang="en">
<head>
<meta charset="utf-8">
<title>TotHaven – Community Connect</title>
<link href="https://fonts.googleapis.com/css2?family=Comic+Neue:wght@400;700&family=Arimo:wght@400;700&display=swap" rel="stylesheet">
<style>
:root{
  --sky-top:#2f9fe0;
  --sky-mid:#8fd3f4;
  --cloud:#eef8fd;
  --grass:#5f9a1e;
  --grass-dark:#4f8417;
  --red:#e8334a;
  --red-dark:#c81f34;
  --orange:#ff7a3a;
  --orange-dark:#ee6322;
  --teal:#1cc2cc;
  --teal-dark:#10a5ae;
  --green:#52b446;
  --purple:#a33ee6;
  --lime:#7cc233;
  --navy:#2a4fb3;
  --sky-tab:#2aa6e8;
  --title:#2d3f9e;
  --ink:#333;
  --white:#fff;
}
*{box-sizing:border-box;margin:0;padding:0}
html,body{width:891px;height:1200px;overflow:hidden}
body{font-family:"Arimo",Arial,sans-serif;color:var(--ink);background:var(--grass)}
.canvas{position:relative;width:891px;height:1200px;overflow:hidden}
.display{font-family:"Comic Neue","Comic Sans MS",cursive}
.scene{position:absolute;inset:0;
  background:
    radial-gradient(ellipse 260px 180px at 130px 330px, rgba(255,120,80,.35), transparent 70%),
    radial-gradient(ellipse 520px 120px at 445px 300px, var(--cloud), transparent 70%),
    linear-gradient(180deg,var(--sky-top) 0,var(--sky-mid) 260px,#d8f0fb 360px,#9ccb3a 430px,var(--grass) 560px,var(--grass) 1200px)}
.logo{position:absolute;left:100px;top:38px;display:flex;align-items:center;gap:8px}
.logo-dot{width:26px;height:26px;border-radius:50%;background:var(--purple)}
.logo-name{font-family:"Comic Neue",cursive;font-weight:700;font-size:36px;color:var(--purple)}
.page-title{position:absolute;left:336px;top:12px;font-size:27px;font-weight:700;color:var(--title)}
.social{position:absolute;display:flex;gap:6px}
.social span{width:20px;height:20px;border-radius:50%;display:block}
.social.top{left:698px;top:18px}
.social.top span{background:var(--navy)}
.social.foot{left:698px;top:1160px}
.social.foot span{background:#7fae2e}
.nav{position:absolute;left:0;top:0}
.nav a{position:absolute;display:flex;align-items:center;justify-content:center;color:var(--white);text-decoration:none;font-family:"Comic Neue",cursive;font-weight:700;font-size:14px;box-shadow:0 2px 3px rgba(0,0,0,.25)}
.login-box{position:absolute;top:180px;height:72px;padding:8px 9px}
.login-box label{display:block;font-family:"Comic Neue",cursive;font-weight:700;color:var(--white);font-size:14px;margin-bottom:5px}
.login-box .field{height:32px;background:var(--white);border-radius:2px}
.user{left:98px;width:260px;background:var(--red)}
.pass{left:366px;width:263px;background:var(--orange)}
.register{position:absolute;left:637px;top:180px;width:157px;height:72px;background:var(--green);color:var(--white);font-size:28px;font-weight:700;display:flex;align-items:center;justify-content:center}
.groups-shape{position:absolute;left:0;top:0}
.groups-title{position:absolute;left:178px;top:292px;font-size:24px;font-weight:700;color:#222}
.groups-photo{position:absolute;left:182px;top:324px;width:136px;height:128px;background:linear-gradient(135deg,#f2d3b0,#d94d6a 50%,#4a8fd6);border:5px solid var(--white);outline:2px solid #567a2a;transform:rotate(2deg)}
.groups-head{position:absolute;left:336px;top:332px;font-size:19px;font-weight:700;color:var(--red-dark)}
.groups-text{position:absolute;left:336px;top:360px;width:370px;font-size:7.6px;line-height:14px;color:#444}
.group-strip{position:absolute;left:172px;top:470px;width:558px;height:108px;background:var(--white)}
.group{position:absolute;top:476px;width:89px;text-align:center}
.group p{font-size:11px;margin-bottom:6px}
.group .thumb{height:76px;border:2px solid}
.btn-dark{position:absolute;left:206px;top:587px;background:#111;color:var(--white);font-size:8px;padding:5px 4px;border-radius:2px}
.col{position:absolute;top:650px;width:226px;height:488px;box-shadow:0 3px 6px rgba(0,0,0,.3)}
.col h2{text-align:center;color:var(--white);font-size:25px;padding-top:2px;height:34px}
.col .media{margin:0 auto;width:193px;height:134px;border:2px solid rgba(255,255,255,.6)}
.col .intro{font-size:8px;line-height:12px;color:rgba(255,255,255,.75);padding:6px 16px 0}
.forum{left:98px;background:linear-gradient(180deg,var(--red),var(--red-dark))}
.acts{left:333px;background:var(--orange)}
.market{left:568px;background:linear-gradient(180deg,var(--teal),var(--teal-dark))}
.topics{list-style:none;padding:8px 0 0 18px}
.topics li{font-size:8.5px;color:var(--white);height:20.8px;position:relative;padding-left:15px}
.topics li::before{content:"";position:absolute;left:0;top:2px;width:5px;height:5px;border-radius:50%;background:var(--white)}
.events{list-style:none;padding:6px 14px 0 16px}
.events li{height:40px;display:flex;gap:8px;align-items:flex-start;border-bottom:1px solid rgba(255,255,255,.3);padding-top:5px}
.events .date{background:var(--red-dark);color:var(--white);font-size:7px;padding:5px 4px;white-space:nowrap}
.events .txt{font-size:8.3px;line-height:10px;color:var(--white)}
.products{display:grid;grid-template-columns:96px 96px;column-gap:2px;row-gap:0;padding:10px 0 0 20px}
.products figure{height:76px;text-align:center}
.products .pic{width:62px;height:52px;margin:0 auto;border:2px solid var(--white)}
.products figcaption{font-size:8px;color:var(--white);margin-top:3px}
.col .go{position:absolute;right:15px;bottom:13px;background:var(--white);color:#333;font-family:"Comic Neue",cursive;font-weight:700;font-size:8px;padding:5px 4px;border-radius:2px}
.kid{position:absolute;top:912px;height:288px;border-radius:40px 40px 0 0}
.kid.left{left:0;width:100px;background:linear-gradient(180deg,#e9c19e 0,#d63b3b 35%,#3d6fa8 60%,#2d5585)}
.kid.right{left:790px;width:101px;background:linear-gradient(180deg,#eac8a8 0,#e46f7a 35%,#8fb4d8 60%,#6f98c4)}
.footer{position:absolute;left:98px;top:1165px;font-size:8px;color:#cfe3a6}
</style>
</head>
<body>
<div class="canvas">
  <div class="scene" role="img" aria-label="Cartoon sky with rainbow, clouds and rolling green hills"></div>

  <div class="logo"><span class="logo-dot"></span><span class="logo-name">TotHaven</span></div>
  <h1 class="page-title display">Community Connect</h1>
  <div class="social top" aria-label="Social links"><span title="chatterbook"></span><span></span><span></span><span></span></div>

  <nav class="nav">
    <a style="left:436px;top:62px;width:55px;height:40px;background:var(--purple);transform:rotate(-2deg)">Home</a>
    <a style="left:487px;top:66px;width:69px;height:40px;background:var(--lime);transform:rotate(2deg)">About Us</a>
    <a style="left:555px;top:63px;width:73px;height:39px;background:var(--orange)">Services</a>
    <a style="left:622px;top:68px;width:68px;height:41px;background:var(--red);transform:rotate(3deg)">Forum</a>
    <a style="left:678px;top:62px;width:70px;height:40px;background:var(--sky-tab);transform:rotate(-2deg)">Activities</a>
    <a style="left:748px;top:68px;width:82px;height:38px;background:var(--navy)">Contact Us</a>
  </nav>

  <div class="login-box user"><label>USER NAME</label><div class="field"></div></div>
  <div class="login-box pass"><label>PASSWORD</label><div class="field"></div></div>
  <div class="register display">REGISTER</div>

  <svg class="groups-shape" width="891" height="640" aria-hidden="true">
    <polygon points="148,282 752,326 714,598 186,620" fill="#5a8a23"/>
    <polygon points="153,288 746,331 709,593 190,614" fill="#eef5f8"/>
    <path d="M172,578 L730,578 L712,592 L192,612 Z" fill="#e62b84" opacity=".75"/>
    <path d="M380,582 L600,580 L560,600 L360,604 Z" fill="#4cae3a" opacity=".8"/>
  </svg>
  <h2 class="groups-title display">Groups!</h2>
  <div class="groups-photo" role="img" aria-label="Photo of a group of smiling children"></div>
  <h3 class="groups-head display">Lorem Ipsum Dolor</h3>
  <p class="groups-text">Lorem ipsum dolor sit amet, consectetur adipiscing elit. In pellentesque tortor eu vestibulum euismod. Aenean euismod nunc vel tortor interdum rhoncus. Donec auctor commodo vehicula. Aliquam pulvinar quis ante ac suscipit. Sed eget magna vel est eleifend interdum.Aliquam lorem risus, aliquet ut lorem id, dapibus varius est. Mauris aliquam tellus ac justo pellentesque, vel ultricies orci placerat. Pellentesque eget eleifend dolor. Ut a nulla quis quam tempus vehicula vitae.</p>
  <div class="group-strip"></div>
  <div class="group" style="left:198px"><p style="color:var(--red)">Group 1</p><div class="thumb" style="border-color:var(--red);background:linear-gradient(135deg,#d9b08e,#5a4a42)" role="img" aria-label="Group photo"></div></div>
  <div class="group" style="left:301px"><p style="color:var(--purple)">Group 2</p><div class="thumb" style="border-color:var(--purple);background:linear-gradient(135deg,#bcd8f2,#8fb4e0)" role="img" aria-label="Group photo"></div></div>
  <div class="group" style="left:404px"><p style="color:var(--lime)">Group 3</p><div class="thumb" style="border-color:var(--lime);background:linear-gradient(180deg,#c99a7a,#fff 60%)" role="img" aria-label="Group photo"></div></div>
  <div class="group" style="left:507px"><p style="color:var(--orange)">Group 4</p><div class="thumb" style="border-color:var(--orange);background:linear-gradient(135deg,#d9a680,#6f8a3a)" role="img" aria-label="Group photo"></div></div>
  <div class="group" style="left:610px"><p style="color:var(--navy)">Group 5</p><div class="thumb" style="border-color:var(--navy);background:linear-gradient(135deg,#e8e8e8,#4a5a6a)" role="img" aria-label="Group photo"></div></div>
  <div class="btn-dark display">Go to Forum</div>

  <section class="col forum">
    <h2 class="display">Forum!</h2>
    <div class="media" role="img" aria-label="Photo of a girl colouring a picture" style="background:linear-gradient(135deg,#8a7a70,#e8c6b0 50%,#d0d6da)"></div>
    <p class="intro">Lorem ipsum dolor sit amet, consectetur adipiscing elit. In pellentesque tortor eu vestibulum euismod. Aenean euismod nunc.</p>
    <ul class="topics">
      <li>Consectrure adipiscing elit, in pellentesque.</li>
      <li>Consectrure adipiscing elit, in pellentesque.</li>
      <li>Consectrure adipiscing elit, in pellentesque.</li>
      <li>Consectrure adipiscing elit, in pellentesque.</li>
      <li>Consectrure adipiscing elit, in pellentesque.</li>
      <li>Consectrure adipiscing elit, in pellentesque.</li>
      <li>Consectrure adipiscing elit, in pellentesque.</li>
      <li>Consectrure adipiscing elit, in pellentesque.</li>
      <li>Consectrure adipiscing elit, in pellentesque.</li>
      <li>Consectrure adipiscing elit, in pellentesque.</li>
    </ul>
    <span class="go">Go to Forum</span>
  </section>

  <section class="col acts">
    <h2 class="display">Activities</h2>
    <div class="media" role="img" aria-label="Photo of children dancing on a lit stage" style="background:linear-gradient(180deg,#7a5a4a,#2fb6e8 60%,#1a8fd0)"></div>
    <p class="intro">Lorem ipsum dolor sit amet, consectetur adipiscing elit. In pellentesque tortor eu vestibulum euismod. Aenean euismod nunc.</p>
    <ul class="events">
      <li><span class="date">05 / JUL</span><span class="txt">Lorem ipsum dolor sit amet, consectet adipiscing.</span></li>
      <li><span class="date">05 / JUL</span><span class="txt">Lorem ipsum dolor sit amet, consectet adipiscing.</span></li>
      <li><span class="date">05 / JUL</span><span class="txt">Lorem ipsum dolor sit amet, consectet adipiscing.</span></li>
      <li><span class="date">05 / JUL</span><span class="txt">Lorem ipsum dolor sit amet, consectet adipiscing.</span></li>
      <li><span class="date">05 / JUL</span><span class="txt">Lorem ipsum dolor sit amet, consectet adipiscing.</span></li>
      <li><span class="date">05 / JUL</span><span class="txt">Lorem ipsum dolor sit amet, consectet adipiscing.</span></li>
    </ul>
    <span class="go">Go to Activities</span>
  </section>

  <section class="col market">
    <h2 class="display">Marketplace</h2>
    <div class="media" role="img" aria-label="Illustration of a busy old market street" style="background:linear-gradient(180deg,#4a5a4a,#d8d0c0 45%,#8a8070)"></div>
    <p class="intro">Lorem ipsum dolor sit amet, consectetur adipiscing elit. In pellentesque tortor eu vestibulum euismod. Aenean euismod nunc.</p>
    <div class="products">
      <figure><div class="pic" role="img" aria-label="Product photo" style="background:linear-gradient(135deg,#d9b08e,#5a4a42)"></div><figcaption>Lorem ipsum dolor</figcaption></figure>
      <figure><div class="pic" role="img" aria-label="Product photo" style="background:linear-gradient(135deg,#bcd8f2,#8fb4e0)"></div><figcaption>Lorem ipsum dolor</figcaption></figure>
      <figure><div class="pic" role="img" aria-label="Product photo" style="background:linear-gradient(180deg,#c99a7a,#fff 60%)"></div><figcaption>Lorem ipsum dolor</figcaption></figure>
      <figure><div class="pic" role="img" aria-label="Product photo" style="background:linear-gradient(135deg,#d9a680,#6f8a3a)"></div><figcaption>Lorem ipsum dolor</figcaption></figure>
      <figure><div class="pic" role="img" aria-label="Product photo" style="background:linear-gradient(135deg,#e8e8e8,#4a5a6a)"></div><figcaption>Lorem ipsum dolor</figcaption></figure>
      <figure><div class="pic" role="img" aria-label="Product photo" style="background:linear-gradient(135deg,#d9b08e,#3a3a3a)"></div><figcaption>Lorem ipsum dolor</figcaption></figure>
    </div>
    <span class="go">Go to Marketplace</span>
  </section>

  <div class="kid left" role="img" aria-label="Photo of a smiling boy in a striped shirt"></div>
  <div class="kid right" role="img" aria-label="Photo of a smiling girl with pigtails"></div>

  <p class="footer">TOTHAVEN© 2013 | ALL RIGHT RESERVED | PRIVACY</p>
  <div class="social foot" aria-label="Social links"><span title="chatterbook"></span><span></span><span></span><span></span></div>
</div>
</body>
</html>
```